" Escritório Jurídico muito novo e moderno. Com uma visao moderna do direito e que busca oferecer um serviço completo e de qualidade, utilizando-se de uma visao empresarial. "

```html
<!DOCTYPE html>
<html lang="pt-BR">
<head>
<meta charset="utf-8">
<title>Moreira Bastos &amp; Teixeira — Papelaria</title>
<link rel="stylesheet" href="https://fonts.googleapis.com/css2?family=Cinzel:wght@600&family=Open+Sans:wght@400;600&display=swap">
<style>
:root{
  --bg:#e9e6e1;
  --ink:#161616;
  --black:#0d0d0d;
  --black-soft:#2a2a2a;
  --paper:#ffffff;
  --grey:#8a8a8a;
  --line:#cfcfcf;
  --gold:#b8955a;
  --gold-light:#e9d8b4;
}
*{box-sizing:border-box;margin:0;padding:0}
html,body{width:1200px;height:1200px;overflow:hidden}
body{background:var(--bg);position:relative;font-family:"Open Sans",Arial,sans-serif;color:var(--ink)}
.piece{position:absolute}

/* brand lockup */
.brand{display:flex;align-items:center;gap:8px}
.brand-square{width:34px;height:34px;background:currentColor;flex:none}
.brand-name{font-family:"Cinzel",Georgia,serif;font-weight:600;line-height:1.05;font-size:15px;letter-spacing:.02em}
.brand-tag{font-size:5px;letter-spacing:.3em;color:var(--grey);margin-top:3px;text-transform:uppercase}
.brand.on-dark{color:var(--paper)}
.brand.sm .brand-square{width:16px;height:16px}
.brand.sm .brand-name{font-size:7px}
.brand.xs .brand-square{width:11px;height:11px}
.brand.xs .brand-name{font-size:5px}
.brand.xs{gap:4px}

.contact{font-size:5px;line-height:1.55;color:var(--grey);text-align:right}
.contact.on-dark{color:#bdbdbd}
.contact strong{color:inherit;font-weight:600}

.decor{position:absolute;background:linear-gradient(135deg,#3a3a3a 0%,#1b1b1b 55%,#0d0d0d 100%)}
.gold-strip{position:absolute;background:linear-gradient(90deg,var(--gold) 0%,var(--gold-light) 50%,#fff 100%)}

/* letterhead */
.letterhead{left:12px;top:43px;width:384px;height:497px;background:var(--paper);padding:36px 34px}
.letterhead .brand{position:absolute;right:30px;top:26px}
.letter-body{margin-top:76px;width:240px;font-size:5.2px;line-height:1.6;color:#444}
.letter-body p{margin-bottom:9px}
.signature{position:absolute;left:195px;top:382px;width:70px;height:22px;background:linear-gradient(90deg,#d7d7d7,#f2f2f2)}
.signer{position:absolute;left:200px;top:408px;font-size:4.5px;color:var(--grey)}
.letter-foot{position:absolute;left:34px;right:34px;bottom:24px;font-size:5px;letter-spacing:.12em;color:var(--grey);text-align:center}

/* open presentation folder */
.folder-top{left:432px;top:43px;width:744px;height:504px;display:flex}
.folder-top .cover-back{position:relative;width:372px;height:100%;background:var(--black);overflow:hidden}
.folder-top .cover-back .decor{left:0;top:0;width:300px;height:280px;opacity:.55}
.folder-top .cover-back .gold-strip{left:26px;top:290px;width:16px;height:214px}
.folder-top .cover-back .contact{position:absolute;right:40px;top:370px}
.folder-top .cover-back .web{position:absolute;right:40px;top:435px;font-size:6px;color:#ddd;letter-spacing:.08em}
.folder-top .cover-front{position:relative;width:372px;height:100%;background:var(--paper)}
.folder-top .rule{position:absolute;left:0;right:0;height:1px;background:var(--line)}
.folder-top .rule.gold{background:linear-gradient(90deg,transparent,var(--gold),transparent)}
.folder-top .cover-front .brand{position:absolute;left:70px;top:212px}
.folder-top .cover-front .brand .brand-square{width:44px;height:44px}
.folder-top .cover-front .brand .brand-name{font-size:19px}

/* small items */
.envelope-label{left:132px;top:586px;width:185px;height:50px;background:var(--paper);clip-path:polygon(0 14%,100% 0,100% 86%,0 100%);display:flex;align-items:center;padding-left:40px}
.cd{left:334px;top:556px;width:112px;height:112px}
.badge{display:flex;flex-direction:column;align-items:center;padding-top:10px;border-radius:3px}
.badge .slot{width:16px;height:3px;border-radius:2px;background:var(--bg);margin-bottom:30px}
.badge-dark{left:461px;top:576px;width:48px;height:108px;background:var(--black)}
.badge-light{left:540px;top:595px;width:60px;height:101px;background:var(--paper)}
.card-light{left:624px;top:595px;width:144px;height:56px;background:var(--paper);padding:9px}
.card-light .contact{position:absolute;right:8px;bottom:6px;font-size:3.6px}
.card-dark{left:792px;top:576px;width:144px;height:78px;background:var(--black);padding:10px}
.card-dark .contact{position:absolute;right:9px;top:10px;font-size:3.8px}
.card-dark .gold-strip{left:10px;bottom:10px;width:124px;height:1px}

/* envelope */
.envelope{left:12px;top:715px;width:492px;height:461px}
.envelope .flap{position:absolute;left:0;top:0;width:100%;height:130px;background:var(--black);clip-path:polygon(8% 100%,22% 0,78% 0,92% 100%)}
.envelope .body{position:absolute;left:0;top:125px;width:100%;height:336px;background:var(--black);overflow:hidden}
.envelope .body .decor{right:0;top:80px;width:240px;height:256px;opacity:.5}
.envelope .band{position:absolute;left:0;top:22px;width:100%;height:60px;background:var(--paper);display:flex;align-items:center;padding-left:40px}
.envelope .band .gold-strip{left:0;bottom:0;width:100%;height:2px}
.envelope .back-brand{position:absolute;left:30px;bottom:70px}

/* bottom folder */
.folder-bottom{left:552px;top:696px;width:624px;height:480px;background:var(--black);overflow:hidden}
.folder-bottom .flap-top{position:absolute;left:0;top:0;width:100%;height:40px;background:#1a1a1a;clip-path:polygon(0 0,100% 0,92% 100%,8% 100%)}
.folder-bottom .pocket{position:absolute;left:26px;top:48px;width:430px;height:372px;background:var(--paper)}
.folder-bottom .pocket .gold-strip{left:0;width:100%;height:1px}
.folder-bottom .pocket .brand{position:absolute;left:92px;top:166px}
.folder-bottom .pocket .brand .brand-square{width:42px;height:42px}
.folder-bottom .pocket .brand .brand-name{font-size:18px}
.folder-bottom .side .contact{position:absolute;right:30px;top:340px}
.folder-bottom .side .brand{position:absolute;right:30px;bottom:30px}
</style>
</head>
<body>

<!-- letterhead -->
<section class="piece letterhead">
  <div class="brand">
    <span class="brand-square"></span>
    <div><div class="brand-name">MOREIRA<br>BASTOS<br>&amp; TEIXEIRA</div><div class="brand-tag">Advogados associados</div></div>
  </div>
  <div class="letter-body">
    <p>Prezado cliente, apresentamos nossa proposta de assessoria jurídica completa, com atendimento próximo, visão empresarial e foco em soluções práticas para cada demanda do seu negócio.</p>
    <p>Nossa equipe acompanha contratos, questões societárias e trabalhistas, sempre com clareza nos prazos, transparência nos custos e comunicação constante durante todo o processo.</p>
    <p>Acreditamos em um direito moderno, ágil e estratégico, capaz de prevenir conflitos e apoiar o crescimento sustentável das empresas que confiam em nosso trabalho diário.</p>
    <p>Ficamos à disposição para uma reunião inicial, na qual poderemos entender melhor suas necessidades e apresentar os próximos passos da nossa parceria.</p>
    <p>Atenciosamente, equipe Moreira Bastos &amp; Teixeira.</p>
  </div>
  <div class="signature" role="img" aria-label="Assinatura manuscrita do advogado responsável"></div>
  <div class="signer">Dr. Paulo Moreira</div>
  <div class="letter-foot">Rua das Acácias, 120 · São Paulo · SP · contato@mbt.com.br · Telefone +55 11 0000-0000</div>
</section>

<!-- open presentation folder -->
<section class="piece folder-top">
  <div class="cover-back">
    <div class="decor" role="img" aria-label="Grandes iniciais decorativas do escritório em tons de cinza"></div>
    <div class="gold-strip"></div>
    <div class="contact on-dark"><strong>Telefone</strong><br>+55 11 0000-0000<br>Rua das Acácias, 120<br>São Paulo · SP<br>contato@mbt.com.br</div>
    <div class="web">www.mbt.com.br</div>
  </div>
  <div class="cover-front">
    <div class="rule" style="top:196px"></div>
    <div class="rule gold" style="top:276px"></div>
    <div class="brand">
      <span class="brand-square"></span>
      <div><div class="brand-name">MOREIRA<br>BASTOS<br>&amp; TEIXEIRA</div><div class="brand-tag">Advogados associados</div></div>
    </div>
  </div>
</section>

<!-- envelope label -->
<div class="piece envelope-label">
  <div class="brand sm"><span class="brand-square"></span><div class="brand-name">MOREIRA<br>BASTOS<br>&amp; TEIXEIRA</div></div>
</div>

<!-- disc -->
<svg class="piece cd" viewBox="0 0 112 112" aria-hidden="true">
  <circle cx="56" cy="56" r="55" fill="#0d0d0d"/>
  <path d="M56 56 L56 1 A55 55 0 0 1 111 56 Z" fill="#ffffff"/>
  <rect x="70" y="26" width="7" height="7" fill="#161616"/>
  <text x="79" y="30" font-family="Cinzel, serif" font-weight="600" font-size="4" fill="#161616">MOREIRA</text>
  <text x="79" y="34.5" font-family="Cinzel, serif" font-weight="600" font-size="4" fill="#161616">BASTOS</text>
  <circle cx="56" cy="56" r="12" fill="#e9e6e1"/>
  <circle cx="56" cy="56" r="12" fill="none" stroke="#bbb" stroke-width=".6"/>
</svg>

<!-- badges -->
<div class="piece badge badge-dark">
  <span class="slot"></span>
  <div class="brand xs on-dark"><span class="brand-square"></span><div class="brand-name">MOREIRA<br>BASTOS</div></div>
</div>
<div class="piece badge badge-light">
  <span class="slot"></span>
  <div class="brand xs"><span class="brand-square"></span><div class="brand-name">MOREIRA<br>BASTOS<br>&amp; TEIXEIRA</div></div>
</div>

<!-- business cards -->
<div class="piece card-light">
  <div class="brand xs"><span class="brand-square"></span><div class="brand-name">MOREIRA<br>BASTOS<br>&amp; TEIXEIRA</div></div>
  <div class="contact">contato@mbt.com.br<br>www.mbt.com.br</div>
</div>
<div class="piece card-dark">
  <div class="contact on-dark"><strong>Paulo Moreira</strong><br>Advogado<br>+55 11 0000-0000</div>
  <div class="gold-strip"></div>
</div>

<!-- envelope -->
<section class="piece envelope">
  <div class="flap"></div>
  <div class="body">
    <div class="decor" role="img" aria-label="Grandes iniciais decorativas do escritório em tons de cinza"></div>
    <div class="band">
      <div class="brand"><span class="brand-square"></span><div><div class="brand-name">MOREIRA<br>BASTOS<br>&amp; TEIXEIRA</div></div></div>
      <div class="gold-strip"></div>
    </div>
    <div class="back-brand">
      <div class="brand sm on-dark"><span class="brand-square"></span><div class="brand-name">MOREIRA<br>BASTOS<br>&amp; TEIXEIRA</div></div>
    </div>
  </div>
</section>

<!-- pocket folder -->
<section class="piece folder-bottom">
  <div class="flap-top"></div>
  <div class="pocket">
    <div class="gold-strip" style="top:150px"></div>
    <div class="brand">
      <span class="brand-square"></span>
      <div><div class="brand-name">MOREIRA<br>BASTOS<br>&amp; TEIXEIRA</div><div class="brand-tag">Advogados associados</div></div>
    </div>
    <div class="gold-strip" style="top:232px"></div>
  </div>
  <div class="side">
    <div class="contact on-dark"><strong>Telefone</strong><br>+55 11 0000-0000<br>Rua das Acácias, 120<br>São Paulo · SP<br>www.mbt.com.br</div>
    <div class="brand sm on-dark"><span class="brand-square"></span><div class="brand-name">MOREIRA<br>BASTOS<br>&amp; TEIXEIRA</div></div>
  </div>
</section>

</body>
</html>
```